Lanternfield Voyages Business Card Design for Home Based Travel Agency

We already have a logo and I would like to see about getting a Business Card Design. The font on the logo can be changed. We are a home based travel agency and sell cruises and tour packages, etc. I would like the following information put into the design Name of Company and Tag Line from the logo. I would also like the email info@lanternfieldvoyages.example Phone 555-238-6140. Website www.lanternfieldvoyages.example. My name Neil Parton Travel Consultant and my wife's Name Mavis Parton. I would like you to use your imagination as nothing is off limites. Impress Me!

Target Market(s)

Baby Boomers

Industry/Entity Type

Travel Agent

Contact Information for Business Card

See above

Font styles to use
Serif
Sans Serif

Colors

Designer to choose colors to be used in the design.

Requirements
Must have
• Play with different fonts and needs to be easily readable, i.e. not too small of print.
Nice to have
• Use your imagination

```html
<!DOCTYPE html>
<html lang="en">
<head>
<meta charset="utf-8">
<title>Lanternfield Voyages – Business Card</title>
<link rel="stylesheet" href="https://fonts.googleapis.com/css2?family=Open+Sans:wght@400;600;700&display=swap">
<style>
  :root {
    --page: #ffffff;
    --slate-light: #a3a4a4;
    --slate-mid: #6b6c6c;
    --slate-dark: #454646;
    --band-grey: #989898;
    --sky: #00ccff;
    --navy: #020466;
    --ink-light: #ffffff;
  }
  html, body {
    margin: 0;
    padding: 0;
    width: 1200px;
    height: 1200px;
    overflow: hidden;
    background: var(--page);
    font-family: "Open Sans", Arial, sans-serif;
  }
  .sheet {
    position: relative;
    width: 1200px;
    height: 1200px;
  }
  .card {
    position: absolute;
    left: 249px;
    width: 702px;
    height: 398px;
    overflow: hidden;
  }
  .card--front { top: 113px; }
  .card--back { top: 689px; }

  .texture {
    position: absolute;
    left: 0;
    top: 0;
    width: 100%;
    background:
      linear-gradient(115deg, var(--slate-light) 0%, var(--slate-mid) 30%, var(--slate-dark) 58%, var(--slate-dark) 100%);
  }
  .card--front .texture { height: 251px; }
  .card--back .texture { height: 100%; }

  .mid-band {
    position: absolute;
    left: 0;
    top: 251px;
    width: 100%;
    height: 55px;
    background: var(--band-grey);
  }
  .contact-strip {
    position: absolute;
    left: 0;
    top: 306px;
    width: 100%;
    height: 92px;
  }

  .holder-name {
    position: absolute;
    left: 51px;
    top: 58px;
    margin: 0;
    font-size: 42px;
    line-height: 1;
    font-weight: 400;
    color: var(--ink-light);
    letter-spacing: 0.5px;
  }
  .holder-name strong { font-weight: 700; }
  .holder-title {
    position: absolute;
    left: 52px;
    top: 104px;
    margin: 0;
    font-size: 17.5px;
    line-height: 1;
    letter-spacing: 4.6px;
    color: var(--ink-light);
  }
  .phone {
    position: absolute;
    right: 48px;
    top: 214px;
    display: flex;
    align-items: center;
    gap: 3px;
    font-size: 24px;
    color: var(--ink-light);
    letter-spacing: 0.3px;
  }
  .phone svg { width: 18px; height: 22px; }

  .web-lines {
    position: absolute;
    right: 103px;
    top: 326px;
    text-align: right;
    color: var(--ink-light);
    font-size: 17px;
    line-height: 29px;
    letter-spacing: 0.2px;
  }
  .globe {
    position: absolute;
    left: 607px;
    top: 320px;
    width: 54px;
    height: 54px;
  }

  .brand {
    position: absolute;
    left: 0;
    width: 100%;
    text-align: center;
    color: var(--ink-light);
  }
  .brand-mark {
    position: absolute;
    left: 327px;
    top: 150px;
    width: 48px;
    height: 48px;
    background: var(--ink-light);
  }
  .brand-name {
    top: 212px;
    margin: 0;
    font-size: 30px;
    font-weight: 400;
    line-height: 1;
    letter-spacing: 1px;
  }
  .brand-tagline {
    top: 268px;
    margin: 0;
    font-size: 10px;
    line-height: 1.2;
    letter-spacing: 0.4px;
  }
  .corner-accent {
    position: absolute;
    left: 0;
    top: 0;
    width: 120px;
    height: 180px;
  }
</style>
</head>
<body>
<div class="sheet">

  <section class="card card--front" aria-label="Business card front">
    <div class="texture" role="img" aria-label="Grey gradient background with faint brushed scratch texture"></div>
    <h1 class="holder-name">NEIL <strong>PARTON</strong></h1>
    <p class="holder-title">TRAVEL CONSULTANT</p>
    <div class="phone">
      <span>555-238-6140</span>
      <svg viewBox="0 0 18 22" aria-hidden="true">
        <path d="M5 1 L8 6 L6 8 C6 11 8 15 11 17 L13 15 L17 19 L14 21 C8 21 2 12 2 4 Z" fill="#ffffff"/>
      </svg>
    </div>
    <div class="mid-band"></div>
    <svg class="contact-strip" viewBox="0 0 702 92" preserveAspectRatio="none" aria-hidden="true">
      <rect width="702" height="92" fill="var(--band-grey)"/>
      <polygon points="0,0 238,0 181,92 0,92" fill="var(--sky)"/>
      <polygon points="274,0 702,0 702,92 217,92" fill="var(--navy)"/>
    </svg>
    <div class="web-lines">
      <div>info@lanternfieldvoyages.example</div>
      <div>www.lanternfieldvoyages.example</div>
    </div>
    <svg class="globe" viewBox="0 0 54 54" aria-hidden="true">
      <circle cx="27" cy="27" r="25" fill="#ffffff"/>
      <g fill="none" stroke="var(--navy)" stroke-width="2">
        <ellipse cx="27" cy="27" rx="11" ry="25"/>
        <line x1="27" y1="2" x2="27" y2="52"/>
        <line x1="2" y1="27" x2="52" y2="27"/>
        <path d="M6 15 H48 M6 39 H48"/>
      </g>
    </svg>
  </section>

  <section class="card card--back" aria-label="Business card back">
    <div class="texture" role="img" aria-label="Grey gradient background with faint brushed scratch texture"></div>
    <svg class="corner-accent" viewBox="0 0 120 180" aria-hidden="true">
      <polygon points="0,0 107,0 0,173" fill="var(--band-grey)"/>
      <polygon points="0,0 71,0 0,115" fill="var(--sky)"/>
    </svg>
    <div class="brand-mark" aria-hidden="true"></div>
    <p class="brand brand-name">Lanternfield Voyages</p>
    <p class="brand brand-tagline">Every Journey is a Tale Worth Telling</p>
  </section>

</div>
</body>
</html>
```